Business card for Les Brisants-Corail campsite

HORIZONTAL / 85x55
OBJECTIVE
Create a modern, attractive and memorable business card for the Les Brisants-Corail campsite, located on the Île d'Oléron.
The map should make people want to discover the campsite and immediately convey its world: ocean, holidays, nature and conviviality.
VISUAL IDENTITY
The design must be in the same graphic style as our website:
www.lesbrisants-corail.fr
The site is the main reference for the visual atmosphere: colours, typography, shapes, photographs and general universe.
The map and the site must give the impression of belonging to a single brand identity.
A UNIVERSE TO TRANSMIT
• Île d'Oléron
• Atlantic Ocean
• Seaside
• Direct access to the beaches
• Vacation
• Nature
• Family-friendly and welcoming atmosphere
• Relaxation
DESIRED STYLE
Bright, warm, modern, nautical and natural.
We want a creation with a real personality, immediately recognizable, and not a generic camping business card.
FRONT
Prioritize visual impact with:
• Official logo Les Brisants-Corail
• Île d'Oléron
• A strong evocation of the ocean and holidays
• A short and memorable hook
The designer is free to propose their own hook.
BACK
The Coral Breakers
Villages 1 & 2
22 Rue des Mouettes
17455 Saint-Ardoin-sur-Mer
France
Tel.: +33 5 47 12 38 04
www.lesbrisants-corail. fr
Possibility of discreet integration:
Direct access to the beaches
Mobile homes • Pitches • Accommodation
Le Varech Bar-Restaurant
FORMAT
Double-sided card: 85 × 55 mm.
Horizontal orientation
AVOID
• Overly institutional design
• Overloaded map
• Generic "camping" style
• Too many pictograms
• Accumulation of texts
• Modification or distortion of the official logo
• Graphic design unrelated to the website
CREATIVE FREEDOM
We are looking for an original proposal.
The designer can play with the graphic codes of the ocean, waves, sun, beach and Île d'Oléron, while remaining faithful to the visual identity of the site.
The card must be aesthetically pleasing and original enough to make people want to keep it.
The objective:
See the map → think about the ocean and holidays → remember Les Brisants-Corail → discover the campsite.
Target Market(s)
All targets
Industry/Entity Type
Tourisme
Contact Information for Business Card
adresse, téléphone, email, site internet + réseaux sociaux
Look and feel
Each slider illustrates characteristics of the customer's brand and the style your logo design should communicate.

```html
<!DOCTYPE html>
<html lang="en">
<head>
<meta charset="utf-8">
<title>Les Brisants-Corail – business card</title>
<link rel="stylesheet" href="https://fonts.googleapis.com/css2?family=Lato:wght@400;700;900&display=swap">
<style>
:root{
  --page:#9a9a9a;
  --card:#ffffff;
  --ink:#4a4c4f;
  --band:#595c5f;
  --sky:#4fc0e3;
  --leaf:#8ccb47;
  --grass:#4ccc00;
  --lime:#e0f014;
  --meadow:#74c800;
  --icon:#3aa8e0;
}
*{margin:0;padding:0;box-sizing:border-box}
html,body{width:1200px;height:1059px;overflow:hidden;background:var(--page);font-family:'Lato',sans-serif;color:var(--ink)}
.card{position:absolute;left:255px;width:704px;height:401px;background:var(--card);border-radius:26px;overflow:hidden}
.card--front{top:79px}
.card--back{top:569px}
.divider{position:absolute;width:2px;background:var(--ink)}
.brand{position:absolute;display:flex;flex-direction:column;justify-content:center}
.brand__row{display:flex;align-items:center;gap:9px}
.brand__dot{width:18px;height:18px;border-radius:50%;flex:none}
.brand__name{font-weight:700;font-size:24px;line-height:1.1;color:var(--ink)}
.brand__village{margin-top:8px;margin-left:27px;font-size:13px;letter-spacing:3px;text-transform:uppercase;color:var(--ink)}
.person{position:absolute;left:41px;top:170px}
.person__name{font-weight:700;font-size:28px;line-height:1.2}
.person__role{font-size:19.5px;margin-top:3px}
.rule{position:absolute;left:41px;top:244px;width:623px;height:2px;background:var(--ink)}
.contacts{position:absolute;left:41px;top:253px;list-style:none}
.contacts li{display:flex;align-items:center;height:29.5px;font-size:19.5px}
.contacts svg{width:22px;height:22px;margin-right:11px}
.address{position:absolute;right:38px;top:255px;text-align:right;font-size:19.5px;line-height:29px}
.accent-line{position:absolute;left:0;right:0;top:346px;height:3px;background:var(--icon)}
.web-band{position:absolute;left:0;right:0;top:350px;bottom:0;background:var(--band);color:#fff;font-weight:700;font-size:40px;text-align:center;line-height:50px}
.offer{position:absolute;left:0;right:0;top:245px;text-align:center;font-size:22.5px;line-height:27px}
.offer strong{font-weight:700}
.stripe{position:absolute;left:0;right:0;bottom:0;height:21px;display:flex}
.stripe span{flex:1}
</style>
</head>
<body>

<section class="card card--front">
  <div class="brand" style="left:95px;top:40px;width:240px;height:110px">
    <div class="brand__row"><span class="brand__dot" style="background:var(--leaf)"></span><span class="brand__name">Les Brisants-Corail</span></div>
    <div class="brand__village">Village 2</div>
  </div>
  <div class="divider" style="left:357px;top:32px;height:121px"></div>
  <div class="brand" style="left:375px;top:40px;width:240px;height:110px">
    <div class="brand__row"><span class="brand__dot" style="background:var(--sky)"></span><span class="brand__name">Les Brisants-Corail</span></div>
    <div class="brand__village">Village 1</div>
  </div>

  <div class="person">
    <div class="person__name">Julien MARCHAND</div>
    <div class="person__role">Management / Direction</div>
  </div>
  <div class="rule"></div>

  <ul class="contacts">
    <li><svg viewBox="0 0 24 24"><path fill="var(--icon)" d="M6.6 10.8c1.4 2.8 3.8 5.1 6.6 6.6l2.2-2.2c.3-.3.7-.4 1-.2 1.1.4 2.300.6 3.6.6.6 0 1 .4 1 1V20c0 .6-.4 1-1 1C10.6 21 3 13.4 3 4c0-.6.4-1 1-1h3.5c.6 0 1 .4 1 1 0 1.3.2 2.5.6 3.6.1.3 0 .7-.2 1z"/></svg>+33 5 47 12 38 04</li>
    <li><svg viewBox="0 0 24 24"><path fill="var(--icon)" d="M6.6 10.8c1.4 2.8 3.8 5.1 6.6 6.6l2.2-2.2c.3-.3.7-.4 1-.2 1.1.4 2.300.6 3.6.6.6 0 1 .4 1 1V20c0 .6-.4 1-1 1C10.6 21 3 13.4 3 4c0-.6.4-1 1-1h3.5c.6 0 1 .4 1 1 0 1.3.2 2.5.6 3.6.1.3 0 .7-.2 1z"/></svg>+33 6 41 27 83 19</li>
    <li><svg viewBox="0 0 24 24"><rect x="1" y="5" width="22" height="15" fill="var(--icon)"/><path d="M1 5l11 8 11-8" fill="none" stroke="#fff" stroke-width="2"/></svg>julien@lesbrisants.net</li>
  </ul>

  <div class="address">
    LES BRISANTS-CORAIL Village 1 &amp; 2<br>
    22 Rue des Mouettes<br>
    17455 Saint-Ardoin-sur-Mer, France
  </div>

  <div class="accent-line"></div>
  <div class="web-band">www.lesbrisants-corail.fr</div>
</section>

<section class="card card--back">
  <div class="brand" style="left:60px;top:40px;width:250px;height:120px">
    <div class="brand__row"><span class="brand__dot" style="background:var(--sky)"></span><span class="brand__name">Les Brisants-Corail</span></div>
  </div>
  <div class="divider" style="left:329px;top:30px;height:139px"></div>
  <div class="brand" style="left:366px;top:40px;width:280px;height:120px">
    <div class="brand__row"><span class="brand__name" style="font-size:40px">Le Varech</span></div>
  </div>

  <p class="offer">
    <strong>Direct access to the beaches</strong><br>
    Mobile homes • Pitches • Accommodation<br>
    • Le Varech Bar-Restaurant
  </p>

  <div class="stripe">
    <span style="background:var(--sky)"></span>
    <span style="background:var(--grass)"></span>
    <span style="background:var(--lime)"></span>
    <span style="background:var(--meadow)"></span>
  </div>
</section>

</body>
</html>
```